Velvet Crypt Mixtape Podcast Design

My audio drama podcast is a funny horror story with romantic elements called Velvet Crypt Mixtape.
I'm looking for a colorful design featuring the title and letting the viewer know this is a horror show.
The title needs to be clearly visible even in thumbnail size.

```html
<!DOCTYPE html>
<html lang="en">
<head>
<meta charset="utf-8">
<title>Velvet Crypt Mixtape – Podcast Cover</title>
<link rel="stylesheet" href="https://fonts.googleapis.com/css2?family=Bangers&family=Creepster&family=Lora:wght@400&display=swap">
<style>
  :root {
    --page-bg: #ffffff;
    --violet-top: #9626e0;
    --magenta-corner: #f255f2;
    --violet-mid: #4f1d8c;
    --night-bottom: #141a24;
    --plum-top: #9a2fc2;
    --plum-mid: #5b1f66;
    --ink-bottom: #171717;
    --title-white: #e4fbf4;
    --title-shade: #4a1580;
    --slime-green: #1dff7a;
    --slime-glow: rgba(40, 255, 130, 0.65);
    --caption-cool: #9aa0c4;
    --caption-grey: #8a8a8a;
  }
  * { box-sizing: border-box; margin: 0; padding: 0; }
  html, body {
    width: 693px;
    height: 1200px;
    overflow: hidden;
    background: var(--page-bg);
  }
  .sheet {
    position: relative;
    width: 693px;
    height: 1200px;
  }
  .cover {
    position: absolute;
    left: 84px;
    width: 525px;
    height: 525px;
    overflow: hidden;
  }
  .cover--violet { top: 51px; }
  .cover--plum { top: 622px; }
  .cover__backdrop {
    position: absolute;
    inset: 0;
  }
  .cover--violet .cover__backdrop {
    background:
      radial-gradient(circle at 100% 0%, var(--magenta-corner) 0%, transparent 45%),
      linear-gradient(180deg, var(--violet-top) 0%, var(--violet-mid) 45%, var(--night-bottom) 80%);
  }
  .cover--plum .cover__backdrop {
    background:
      radial-gradient(circle at 100% 0%, var(--magenta-corner) 0%, transparent 45%),
      linear-gradient(180deg, var(--plum-top) 0%, var(--plum-mid) 50%, var(--ink-bottom) 80%);
  }
  .cover__title {
    position: absolute;
    inset: 0;
    font-weight: 400;
  }
  .cover__line {
    position: absolute;
    left: 0;
    width: 100%;
    text-align: center;
    line-height: 1;
    white-space: nowrap;
    font-family: "Bangers", "Impact", sans-serif;
    letter-spacing: 2px;
    color: var(--title-white);
    text-shadow: 0 5px 0 var(--title-shade), 0 7px 0 var(--title-shade);
  }
  .cover__line--top { top: 174px; font-size: 64px; }
  .cover__line--drip {
    top: 236px;
    font-family: "Creepster", "Impact", cursive;
    font-size: 104px;
    letter-spacing: 10px;
    color: var(--slime-green);
    text-shadow: 0 0 14px var(--slime-glow), 0 0 28px var(--slime-glow);
  }
  .cover__line--bottom { top: 318px; font-size: 74px; }
  .cover__caption {
    position: absolute;
    left: 0;
    top: 476px;
    width: 100%;
    text-align: center;
    font-family: "Lora", Georgia, serif;
    font-size: 7px;
    line-height: 1.4;
  }
  .cover--violet .cover__caption { color: var(--caption-cool); }
  .cover--plum .cover__caption { color: var(--caption-grey); }
</style>
</head>
<body>
  <main class="sheet">
    <section class="cover cover--violet">
      <div class="cover__backdrop" role="img" aria-label="Photo backdrop: shadowy figure behind frosted glass in violet light"></div>
      <h1 class="cover__title">
        <span class="cover__line cover__line--top">Velvet</span>
        <span class="cover__line cover__line--drip">Crypt</span>
        <span class="cover__line cover__line--bottom">Mixtape</span>
      </h1>
      <p class="cover__caption">Lorem ipsum dolor sit amet, consectetur adipisicing elit, sed do eiusmod<br>tempor incididunt ut labore et dolore magna aliqua.</p>
    </section>

    <section class="cover cover--plum">
      <div class="cover__backdrop" role="img" aria-label="Photo backdrop: shadowy figure behind frosted glass in plum light"></div>
      <h1 class="cover__title">
        <span class="cover__line cover__line--top">Velvet</span>
        <span class="cover__line cover__line--drip">Crypt</span>
        <span class="cover__line cover__line--bottom">Mixtape</span>
      </h1>
      <p class="cover__caption">Lorem ipsum dolor sit amet, consectetur adipisicing elit, sed do eiusmod<br>tempor incididunt ut labore et dolore magna aliqua.</p>
    </section>
  </main>
</body>
</html>
```